Important Solar Energy Company Needs a Stationery Design

I need a modern, attractive, corporate stationary design (letter head and business card)
Attached Company Logo

Target Market(s)

Upmarket

Industry/Entity Type

Business

Colors
ec1f27
ffffff
757575
cbcbcb
000000

```html
<!DOCTYPE html>
<html lang="en">
<head>
<meta charset="utf-8">
<title>Solariva Stationery</title>
<link href="https://fonts.googleapis.com/css2?family=Montserrat:wght@500;600&family=Open+Sans:wght@400;600;700&family=Exo+2:wght@500&display=swap" rel="stylesheet">
<style>
  :root {
    --red: #ec1f27;
    --white: #ffffff;
    --grey: #757575;
    --light: #cbcbcb;
    --black: #000000;
    --stage: #eceff1;
    --blue-a: #2c4fb8;
    --blue-b: #19a6e6;
  }
  * { box-sizing: border-box; margin: 0; padding: 0; }
  html, body { width: 1200px; height: 937px; overflow: hidden; }
  body { background: var(--stage); font-family: "Open Sans", Arial, sans-serif; position: relative; }

  .sheet { position: absolute; background: var(--white); overflow: hidden; }
  .footer-band { position: absolute; left: 0; bottom: 0; width: 100%; display: block; }

  .brand { position: absolute; display: flex; align-items: center; font-family: "Montserrat", Arial, sans-serif; font-weight: 500; color: var(--black); letter-spacing: 0.08em; white-space: nowrap; }
  .brand-dot { border-radius: 50%; background: var(--red); flex: none; }

  /* Letterhead */
  .letterhead { left: 185px; top: 68px; width: 386px; height: 544px; }
  .letterhead .brand { left: 18px; top: 30px; font-size: 15px; }
  .letterhead .brand-dot { width: 26px; height: 26px; margin-right: 8px; }
  .contact { position: absolute; right: 16px; top: 20px; text-align: right; font-size: 4.6px; line-height: 8.4px; color: #333; }
  .contact strong { font-weight: 700; }
  .contact .ico { display: inline-block; width: 4px; height: 4px; border-radius: 1px; background: #555; margin-left: 3px; vertical-align: middle; }
  .letter-body { position: absolute; left: 36px; top: 138px; width: 300px; font-size: 5.2px; line-height: 7.4px; color: #444; }
  .letter-body p { margin-bottom: 8px; }
  .letter-body .para { margin-bottom: 22px; }
  .letter-body .name { font-weight: 700; color: #222; }
  .signature { width: 26px; height: 14px; background: linear-gradient(90deg, #333, #777); opacity: 0.35; border-radius: 7px; margin: -2px 0 6px; }

  /* Cover */
  .cover { left: 636px; top: 41px; width: 458px; height: 575px; }
  .cover .brand { left: 0; right: 0; top: 222px; flex-direction: column; font-size: 34px; letter-spacing: 0.1em; }
  .cover .brand-dot { width: 84px; height: 84px; margin-bottom: 22px; }

  /* Business cards */
  .card { width: 175px; height: 100px; }
  .card-front { left: 46px; top: 658px; }
  .card-front .brand { left: 8px; top: 20px; font-size: 8px; }
  .card-front .brand-dot { width: 13px; height: 13px; margin-right: 4px; }
  .card-person { position: absolute; right: 6px; top: 28px; text-align: right; font-size: 4.4px; line-height: 6.4px; color: #333; }
  .card-person .who { font-weight: 700; font-size: 5px; }
  .card-person .bar { position: absolute; right: -6px; top: 0; width: 3px; height: 12px; background: var(--black); }
  .card-person .gap { height: 6px; }
  .card-address { position: absolute; left: 6px; bottom: 6px; font-size: 4.2px; line-height: 5.6px; color: var(--white); font-weight: 600; }
  .card-back { left: 46px; top: 785px; height: 99px; }
  .card-back .brand { left: 0; right: 0; top: 42px; justify-content: center; font-size: 10px; }
  .card-back .brand-dot { width: 17px; height: 17px; margin-right: 5px; }

  /* Envelopes */
  .envelope-front { left: 265px; top: 671px; width: 432px; height: 209px; }
  .envelope-front .brand { left: 14px; top: 20px; font-size: 15px; }
  .envelope-front .brand-dot { width: 26px; height: 26px; margin-right: 12px; }
  .envelope-back { left: 737px; top: 672px; width: 431px; height: 208px; }
  .flap { position: absolute; left: 0; top: 0; width: 100%; height: 71px; border-radius: 0 0 34px 34px; background: linear-gradient(90deg, var(--blue-a), var(--blue-b) 55%, var(--blue-a)); display: flex; align-items: center; justify-content: center; }
  .flap span { font-family: "Exo 2", Arial, sans-serif; font-weight: 500; color: var(--white); font-size: 13px; letter-spacing: 0.22em; }
</style>
</head>
<body>

  <!-- Letterhead -->
  <section class="sheet letterhead">
    <div class="brand"><span class="brand-dot"></span>SOLARIVA</div>
    <div class="contact">
      <strong>12 Harbour Way</strong><br>
      <strong>Westfield Park 04</strong><br>
      012 345 6789<span class="ico"></span><br>
      012 345 6790<span class="ico"></span><br>
      012 345 6791<span class="ico"></span><br>
      info@solariva.com<span class="ico"></span><br>
      www.solariva.com<span class="ico"></span>
    </div>
    <div class="letter-body">
      <p>July 2, 2012</p>
      <p><span class="name">Dear Cli,</span><br>ABC Building, def St., Country Name</p>
      <p>Lorem ipsum dolor sit amet, consectetur adipiscing elit, sed do eiusmod tempor incididunt ut labore et dolore magna aliqua. Ut enim ad minim veniam, quis nostrud exercitation ullamco laboris nisi ut aliquip ex ea commodo consequat. Duis aute irure dolor in reprehenderit in voluptate velit esse cillum dolore eu fugiat nulla pariatur. Excepteur sint occaecat cupidatat non proident, sunt in culpa qui officia deserunt mollit anim id est laborum, sed ut perspiciatis unde omnis iste natus error sit voluptatem.</p>
      <p class="para">Lorem ipsum dolor sit amet, consectetur adipiscing elit, sed do eiusmod tempor incididunt ut labore et dolore magna aliqua. Ut enim ad minim veniam, quis nostrud exercitation ullamco laboris nisi ut aliquip.</p>
      <p>Lorem ipsum dolor sit amet, consectetur adipiscing elit, sed do eiusmod tempor incididunt ut labore et dolore magna aliqua. Ut enim ad minim veniam, quis nostrud exercitation ullamco laboris nisi ut aliquip ex ea commodo consequat. Duis aute irure dolor in reprehenderit in voluptate velit esse cillum dolore eu fugiat nulla pariatur. Excepteur sint occaecat cupidatat non proident, sunt in culpa qui officia deserunt mollit anim id est laborum, sed ut perspiciatis unde omnis iste natus error sit voluptatem.</p>
      <p>Best Regards,</p>
      <div class="signature" role="img" aria-label="Handwritten signature"></div>
      <p><span class="name">Daniel Reyes</span><br>Director<br><br>ABC Building, def St., Country Name</p>
    </div>
    <svg class="footer-band" viewBox="0 0 386 80" height="80" preserveAspectRatio="none" aria-hidden="true">
      <path d="M0,20 Q193,0 386,20 L386,80 L0,80 Z" fill="var(--red)"/>
    </svg>
  </section>

  <!-- Presentation cover -->
  <section class="sheet cover">
    <div class="brand"><span class="brand-dot"></span>SOLARIVA</div>
    <svg class="footer-band" viewBox="0 0 458 90" height="90" preserveAspectRatio="none" aria-hidden="true">
      <path d="M0,22 Q229,0 458,22 L458,90 L0,90 Z" fill="var(--red)"/>
    </svg>
  </section>

  <!-- Business card front -->
  <section class="sheet card card-front">
    <div class="brand"><span class="brand-dot"></span>SOLARIVA</div>
    <div class="card-person">
      <span class="bar"></span>
      <div class="who">Daniel Reyes</div>
      <div>Managing Director</div>
      <div class="gap"></div>
      012 345 6789<br>012 345 6790<br>012 345 6791<br>info@solariva.com
    </div>
    <svg class="footer-band" viewBox="0 0 175 18" height="18" preserveAspectRatio="none" aria-hidden="true">
      <path d="M0,5 Q87,0 175,5 L175,18 L0,18 Z" fill="var(--red)"/>
    </svg>
    <div class="card-address">12 Harbour Way, Westfield Park 04</div>
  </section>

  <!-- Business card back -->
  <section class="sheet card card-back">
    <div class="brand"><span class="brand-dot"></span>SOLARIVA</div>
  </section>

  <!-- Envelope front -->
  <section class="sheet envelope-front">
    <div class="brand"><span class="brand-dot"></span>SOLARIVA</div>
    <svg class="footer-band" viewBox="0 0 432 50" height="50" preserveAspectRatio="none" aria-hidden="true">
      <path d="M0,16 Q216,0 432,16 L432,50 L0,50 Z" fill="var(--red)"/>
    </svg>
  </section>

  <!-- Envelope back -->
  <section class="sheet envelope-back">
    <div class="flap"><span>www.solariva.com</span></div>
  </section>

</body>
</html>
```